RM Tomás Rivera (Business Card)

Hi designers, in this work, I'm looking for an sophisticated stylish, elegant and proffesional personal card. We have a laboratory of pathology automated, with equipments high quality.
In this web the designers, have created my business logo, the name is "RM Tomás Rivera"
In our lab, we principal work is to prepare the biopsies for further diagnostic of diseases like cancer, tumors, etc.
I need that the first face, only having my complete logo (Rm Tomás Rivera, Laboratorio de procesamiento Histologico)
The overleaf, could repeat the same logo, like water logo.
In this face, I need to say: My full data:

Técnico en Anatomía Patológica
Tomás Rivera Ibarra M.P 47203
Av. Paredes Luján 418 - 2do piso - Instituto Marbel.
Córdoba, Argentina
(0351) 154820937
rivera.tomas@correolab.example

with respect the colors of card, use your imagination, the original logo color is violet, I haven't chosen a color base for the card.

attached pictures are examples of cards I like your DESIGN.
Attached too, the original logo to my company.

the size of card are:
horizontal: 9cm
vertical: 5,5cm

any question that you have, not doubt to question me,
Hand to work!

Industry/Entity Type

Laboratory

Requirements
Must have
• designers sophisticated, not simples, like show the images attached

```html
<!DOCTYPE html>
<html lang="es">
<head>
<meta charset="utf-8">
<title>RM Tomás Rivera · Tarjeta personal</title>
<link rel="stylesheet" href="https://fonts.googleapis.com/css2?family=PT+Sans:ital,wght@0,400;1,400&family=PT+Sans+Narrow:wght@400&family=Open+Sans:wght@300&display=swap">
<style>
  :root {
    --stage: #6e6f71;
    --violet: #5f2180;
    --violet-text: #5a2a82;
    --rule-grey: #7f8083;
    --ink-grey: #6d6e70;
    --paper: #ffffff;
  }
  * { margin: 0; padding: 0; box-sizing: border-box; }
  html, body { width: 1200px; height: 392px; overflow: hidden; }
  body { background: var(--stage); position: relative; font-family: "PT Sans", sans-serif; }

  .card { position: absolute; width: 506px; height: 292px; overflow: hidden; }
  .card--front { left: 87px; top: 55px; background: var(--violet); }
  .card--back { left: 624px; top: 50px; background: var(--paper); }

  .lockup { position: absolute; left: 0; right: 0; text-align: center; }
  .lockup__name {
    font-family: "Open Sans", sans-serif; font-weight: 300;
    letter-spacing: 0.32em; text-transform: uppercase; white-space: nowrap;
    display: inline-flex; align-items: center; gap: 12px;
  }
  .lockup__mark { width: 12px; height: 12px; display: inline-block; }
  .lockup__rule { height: 5px; margin: 2px auto 0; background: var(--rule-grey); }
  .lockup__tagline {
    font-family: "PT Sans Narrow", sans-serif; text-transform: uppercase; white-space: nowrap;
  }

  .card--front .lockup { top: 150px; }
  .card--front .lockup__name { color: var(--paper); font-size: 19px; }
  .card--front .lockup__mark { background: var(--paper); }
  .card--front .lockup__rule { width: 292px; }
  .card--front .lockup__tagline { color: var(--paper); font-size: 23px; margin-top: 4px; }

  .card--back .lockup { top: 70px; }
  .card--back .lockup__name { color: var(--ink-grey); font-size: 14px; }
  .card--back .lockup__mark { background: var(--violet); width: 9px; height: 9px; }
  .card--back .lockup__rule { width: 240px; height: 4px; }
  .card--back .lockup__tagline { color: var(--ink-grey); font-size: 17px; margin-top: 1px; }
  .role-title {
    position: absolute; left: 0; right: 0; top: 127px; text-align: center;
    font-style: italic; font-size: 15px; color: var(--violet-text);
  }

  .wave { position: absolute; left: 0; top: 0; }
  .contact { position: absolute; color: var(--paper); font-size: 13.5px; line-height: 20px; }
  .contact--right { right: 17px; top: 205px; text-align: right; }
  .contact--left { left: 16px; top: 242px; }
</style>
</head>
<body>
  <section class="card card--front" aria-label="Frente">
    <div class="lockup">
      <div class="lockup__name"><span class="lockup__mark"></span>Tomás Rivera</div>
      <div class="lockup__rule"></div>
      <div class="lockup__tagline">Laboratorio de procesamiento histologico</div>
    </div>
  </section>

  <section class="card card--back" aria-label="Dorso">
    <div class="lockup">
      <div class="lockup__name"><span class="lockup__mark"></span>Tomás Rivera</div>
      <div class="lockup__rule"></div>
      <div class="lockup__tagline">Laboratorio de procesamiento histologico</div>
    </div>
    <p class="role-title">Técnico en Anatomía Patológica</p>

    <svg class="wave" width="506" height="292" viewBox="0 0 506 292" aria-hidden="true">
      <path d="M0 208 C170 200 350 175 506 124 L506 134 C350 182 170 206 0 212 Z" fill="#8a8b8d"/>
      <path d="M0 214 C170 208 350 186 506 136 L506 292 L0 292 Z" fill="var(--violet)"/>
    </svg>

    <div class="contact contact--right">
      Tomás Rivera Ibarra M.P 47203<br>
      Av. Paredes Luján 418 - 2do piso<br>
      Instituto Marbel.<br>
      Córdoba, Argentina
    </div>
    <div class="contact contact--left">
      (0351) 154820937<br>
      rivera.tomas@correolab.example
    </div>
  </section>
</body>
</html>
```